Psychiatrist/ Psychotherapist needs a letterhead design

I am a Psychiatrist working in private practice. I work as a psychotherapist and treat patients with depression, anxiety, post traumatic stress and relationship problems. I need a letterhead which is elegant and professional. I would like to see designs using colours such as blues and greys.
I would like the information on the letterhead split between the top and bottom of the page to give it a look of balance.
I want it to look elegant, feminine and upmarket. I don't want it to look too corporate but to show some flair and to be a bit artistic.

Target Market(s)

Other doctors, specialists and agencies who have referred patients to me.

Industry/Entity Type

Work

Font styles to use
Script

Requirements
Must have
• My name and my profession psychiatrist need to be highlighted and prominent. It needs to be professional looking and elegant without being old fashioned or too conservative.
Nice to have
• Balance between the top and bottom of the page.
Should not have
• I don't want fonts which are old and too traditional.

```html
<!DOCTYPE html>
<html lang="en">
<head>
<meta charset="utf-8">
<title>Dr Miriam Ashcombe – Letterhead</title>
<link rel="stylesheet" href="https://fonts.googleapis.com/css2?family=Quicksand:wght@400;500&family=Delius&display=swap">
<style>
  :root {
    --backdrop: #e6e7e8;
    --paper: #ffffff;
    --ink: #6b6f73;
    --ink-dark: #3f4346;
    --rule: #8a8e92;
    --mist-strong: rgba(206, 234, 234, 0.75);
    --mist-mid: rgba(214, 238, 238, 0.45);
    --mist-clear: rgba(214, 238, 238, 0);
  }

  * { box-sizing: border-box; margin: 0; padding: 0; }

  html, body {
    width: 1200px;
    height: 1162px;
    overflow: hidden;
    background: var(--backdrop);
  }

  .letterhead {
    position: absolute;
    left: 220px;
    top: 43px;
    width: 760px;
    height: 1076px;
    background: var(--paper);
    box-shadow: 0 2px 6px rgba(0, 0, 0, 0.08);
    overflow: hidden;
  }

  .flourish {
    position: absolute;
    top: 0;
    left: 100px;
    width: 620px;
    height: 520px;
    background:
      radial-gradient(ellipse 200px 150px at 300px 90px, var(--mist-strong) 0%, var(--mist-clear) 100%),
      radial-gradient(ellipse 180px 200px at 430px 260px, var(--mist-mid) 0%, var(--mist-clear) 100%),
      radial-gradient(ellipse 150px 130px at 180px 200px, var(--mist-mid) 0%, var(--mist-clear) 100%);
    opacity: 0.6;
  }

  .masthead {
    position: absolute;
    top: 30px;
    left: 40px;
    right: 40px;
  }

  .practitioner {
    font-family: "Quicksand", sans-serif;
    font-weight: 400;
    color: var(--ink);
    font-size: 33px;
    line-height: 1.02;
    letter-spacing: -0.3px;
  }

  .practitioner .role { display: block; }

  .email {
    position: absolute;
    top: 120px;
    right: 0;
    font-family: "Quicksand", sans-serif;
    font-size: 17px;
    color: var(--ink-dark);
    letter-spacing: 0.3px;
  }

  .masthead-rule {
    position: absolute;
    top: 150px;
    left: 250px;
    width: 460px;
    height: 2px;
    background: var(--rule);
  }

  .footer {
    position: absolute;
    bottom: 34px;
    left: 0;
    right: 0;
    font-family: "Delius", sans-serif;
    color: var(--ink-dark);
  }

  .footer-rule {
    width: 350px;
    height: 2px;
    margin: 0 0 10px 120px;
    background: var(--rule);
  }

  .address {
    font-size: 17px;
    margin-left: 132px;
    letter-spacing: 0.4px;
  }

  .contacts {
    margin-top: 8px;
    margin-left: 40px;
    font-size: 17px;
    letter-spacing: 0.5px;
    word-spacing: 2px;
  }

  .contacts span + span { margin-left: 12px; }
</style>
</head>
<body>
  <main class="letterhead">
    <div class="flourish" role="img" aria-label="Faint pale teal flowing swirl decoration"></div>

    <header class="masthead">
      <h1 class="practitioner">
        <span class="role">Dr Miriam Ashcombe</span>
        <span class="role">B.Med, FRANZCP</span>
        <span class="role">Psychiatrist</span>
      </h1>
      <p class="email">mashcombe@westmail.net.au</p>
    </header>
    <div class="masthead-rule"></div>

    <footer class="footer">
      <div class="footer-rule"></div>
      <p class="address">14 Carlin Street, Norwood, SA 5067</p>
      <p class="contacts">
        <span>Tel: (08) 8123 4567</span>
        <span>Fax:(08) 8123 4590</span>
        <span>Mob: 0400123987</span>
      </p>
    </footer>
  </main>
</body>
</html>
```